Creation of a Velmora Flyer design

As part of the cr% 26 # 233; ation of our soci% 26 # 233; t% 26 # 233 ;, we wish to cr% 26 # 233; er a flyer pr% 26 # 233; feeling our diff% 26 # 233; annuities% 26 # 233; s business advisory services% 26 # 233; foreign% 26 # 232; res who wish to develop their activities% 26 # 233; s in Switzerland. We want a double-sided flyer that presents% 26 # 233; society% 26 # 233; t% 26 # 233; d% 26 # 39; a c% 26 # 244; t% 26 # 233; and who presents% 26 # 233; benefits of the other. We have d% 26 # 233; j% 26 # 224; made a very basic provisional flyer to be able to present our activities. We put it to you as an example.

Target Market(s)

European companies% 26 # 233; internal% 26 # 233; res% 26 # 233; es by the market% 26 # 233; Swiss

Industry/Entity Type

Business Consultant

Colors

Designer to choose colors to be used in the design.

Requirements
Must have
• Company name and contact details
A field to detail the services
Nice to have
• Some% 26 # 233; l% 26 # 233; elements that recall Switzerland and some% 26 # 233; l% 26 # 233; elements that recall c% 26 # 244; t% 26 # 233; % 26quot; business% 26quot;

```html
<!DOCTYPE html>
<html lang="en">
<head>
<meta charset="utf-8">
<title>Velmora – Swiss Market Flyer</title>
<link href="https://fonts.googleapis.com/css2?family=Roboto+Condensed:wght@300;400&display=swap" rel="stylesheet">
<style>
  :root {
    --stage: #6b6c6e;
    --paper-top: #f4f4f5;
    --paper-bottom: #d9d9db;
    --ink: #2b2b2e;
    --tick: #2f6db5;
    --band-blue: #323c85;
    --band-purple: #6e2f78;
    --footer-text: #e4ddf0;
  }
  * { box-sizing: border-box; margin: 0; padding: 0; }
  html, body {
    width: 1200px; height: 1200px; overflow: hidden;
    background: var(--stage);
  }
  .flyer {
    position: absolute; left: 160px; top: 30px;
    width: 881px; height: 1140px;
    background: linear-gradient(180deg, var(--paper-top) 55%, var(--paper-bottom) 100%);
    font-family: "Roboto Condensed", "Arial Narrow", sans-serif;
    color: var(--ink);
    overflow: hidden;
  }
  .hero-photo {
    position: absolute; left: 0; top: 0; width: 881px; height: 604px;
    background:
      linear-gradient(180deg, rgba(255,255,255,0) 60%, rgba(70,90,130,.55) 100%),
      linear-gradient(160deg, #6aa6e0 0%, #a9cdef 30%, #8a6a4a 55%, #a5432c 75%, #4d5a77 100%);
  }
  .headline-box {
    position: absolute; left: 0; top: 399px; width: 730px; height: 242px;
    background: linear-gradient(180deg, rgba(35,20,55,.55) 0%, rgba(55,45,120,.8) 70%, rgba(70,55,140,.95) 100%),
                linear-gradient(90deg, var(--band-blue), var(--band-purple));
    padding: 19px 0 0 41px;
  }
  .headline {
    font-weight: 400; font-size: 43px; line-height: 53px;
    color: #fff; letter-spacing: 0.2px;
  }
  .intro {
    position: absolute; left: 27px; top: 663px; width: 830px;
    font-weight: 300; font-size: 18.5px; line-height: 22.6px;
  }
  .services {
    position: absolute; top: 752px; list-style: none;
    font-weight: 300; font-size: 17.6px; line-height: 21.4px;
  }
  .services--left { left: 27px; width: 390px; }
  .services--right { left: 447px; width: 410px; }
  .services li {
    position: relative; padding-left: 21px; margin-bottom: 21px;
  }
  .services li svg {
    position: absolute; left: 0; top: 5px; width: 13px; height: 11px;
  }
  .footer {
    position: absolute; left: 0; bottom: 0; width: 881px; height: 70px;
    background: linear-gradient(90deg, var(--band-blue), var(--band-purple));
    color: var(--footer-text);
    text-align: center; font-weight: 300; font-size: 14.6px; line-height: 18px;
    padding-top: 15px;
  }
</style>
</head>
<body>
  <article class="flyer">
    <div class="hero-photo" role="img" aria-label="Photograph of a covered wooden bridge with flower boxes and a stone water tower on a lake, mountains and city buildings behind"></div>

    <div class="headline-box">
      <h1 class="headline">You are convinced of the potential of<br>your product or service and you wish<br>to focus on the Swiss market, or you<br>want to expand your market share!</h1>
    </div>

    <p class="intro">Thanks to its personalized approach and tailor-made assistance, Velmora offers you the right support to develop your business activities and answers to all you questions about the Swiss market. As a partner we assist you in finding market opportunities:</p>

    <ul class="services services--left">
      <li><svg viewBox="0 0 13 11"><path d="M1 6 L4.8 9.5 L12 1.5" fill="none" stroke="var(--tick)" stroke-width="2.6" stroke-linecap="round" stroke-linejoin="round"/></svg>By providing commercial contacts that match your target profiles;</li>
      <li><svg viewBox="0 0 13 11"><path d="M1 6 L4.8 9.5 L12 1.5" fill="none" stroke="var(--tick)" stroke-width="2.6" stroke-linecap="round" stroke-linejoin="round"/></svg>By listing the legal and regulatory requirements specific to the Swiss market (Switzerland is not an EU member State);</li>
      <li><svg viewBox="0 0 13 11"><path d="M1 6 L4.8 9.5 L12 1.5" fill="none" stroke="var(--tick)" stroke-width="2.6" stroke-linecap="round" stroke-linejoin="round"/></svg>By putting you in contact with private or public interlocutors in the contex of an individual contact programme;</li>
      <li><svg viewBox="0 0 13 11"><path d="M1 6 L4.8 9.5 L12 1.5" fill="none" stroke="var(--tick)" stroke-width="2.6" stroke-linecap="round" stroke-linejoin="round"/></svg>By preparing a market study that measures the potential of your product or service;</li>
    </ul>

    <ul class="services services--right">
      <li><svg viewBox="0 0 13 11"><path d="M1 6 L4.8 9.5 L12 1.5" fill="none" stroke="var(--tick)" stroke-width="2.6" stroke-linecap="round" stroke-linejoin="round"/></svg>By adapting your marketing material (website, brochures, flyers, etc.) to the specific of the Swiss market and by translating it into German and/or French;</li>
      <li><svg viewBox="0 0 13 11"><path d="M1 6 L4.8 9.5 L12 1.5" fill="none" stroke="var(--tick)" stroke-width="2.6" stroke-linecap="round" stroke-linejoin="round"/></svg>By organizing a promotional event that is tailored to your needs;</li>
      <li><svg viewBox="0 0 13 11"><path d="M1 6 L4.8 9.5 L12 1.5" fill="none" stroke="var(--tick)" stroke-width="2.6" stroke-linecap="round" stroke-linejoin="round"/></svg>By representing you at trade shows or fairs;</li>
      <li><svg viewBox="0 0 13 11"><path d="M1 6 L4.8 9.5 L12 1.5" fill="none" stroke="var(--tick)" stroke-width="2.6" stroke-linecap="round" stroke-linejoin="round"/></svg>By assuming the fiscal representation of your company;</li>
      <li><svg viewBox="0 0 13 11"><path d="M1 6 L4.8 9.5 L12 1.5" fill="none" stroke="var(--tick)" stroke-width="2.6" stroke-linecap="round" stroke-linejoin="round"/></svg>By offering you logistical and administrative support</li>
    </ul>

    <footer class="footer">
      Neuchâtel Office &nbsp;|&nbsp; Velmora Sàrl &nbsp;|&nbsp; Rue des Tilleuls 14 &nbsp;|&nbsp; 2017 Boudry (Neuchâtel)<br>
      +41 (0)32 000 14 27 &nbsp;|&nbsp; info@velmora.ch &nbsp;|&nbsp; www.velmora.ch
    </footer>
  </article>
</body>
</html>
```